Calder Pizza - Takeout Menu Design

We are looking for a takeout menu design.
We are looking for a( 5" x 8.5" DOUBLE SIDED) flyer with our available pizza flavors
Must be easy to ready and not "busy"

Must include our logo (attached)
website: www.calderpizza.ca
address:
Fenwick Ridge Plaza
417, 318 9 Avenue SW
and the following details:
Visit our website for our complete appetizer, pasta, salad and catering menu.

Winner of this contest will also be offered to create a few print designs via printhive.

Please do not hesitate to ask any questions.

Target Market(s)

Business / Office clientele

Industry/Entity Type

Pizza place / specializing in corporate orders

Requirements
Must have
• Easy to read
Should not have
• Can not be busy or cluttered

```html
<!DOCTYPE html>
<html lang="en">
<head>
<meta charset="utf-8">
<title>Calder Pizza – Take-Out Menu</title>
<link rel="stylesheet" href="https://fonts.googleapis.com/css2?family=Source+Sans+3:wght@400;600&display=swap">
<style>
  :root {
    --backdrop: #2b2b2b;
    --paper: #efeee9;
    --ink: #1c1c1c;
    --brand-red: #b3282c;
    --rule-red: #e2472f;
    --menu-red: #c0383a;
    --on-red: #ffffff;
    --on-red-soft: #f6dada;
    --crust-light: #f7c766;
    --crust-deep: #e59a3a;
  }
  * { margin: 0; padding: 0; box-sizing: border-box; }
  html, body { width: 1200px; height: 1200px; overflow: hidden; }
  body {
    background: var(--backdrop);
    font-family: "Source Sans 3", "Myriad Pro", Arial, sans-serif;
    position: relative;
  }
  .page {
    position: absolute;
    top: 176px;
    width: 498px;
    height: 848px;
    overflow: hidden;
    box-shadow: 0 6px 18px rgba(0,0,0,.45);
  }
  /* ---------- front ---------- */
  .page--front { left: 85px; background: var(--paper); color: var(--ink); }
  .hero-art {
    position: absolute;
    left: 250px; top: -30px;
    width: 500px; height: 500px;
    border-radius: 50%;
    background: radial-gradient(circle at 45% 50%, var(--crust-light) 0%, #f4b04e 55%, var(--crust-deep) 80%, #c9772a 100%);
  }
  .brand {
    position: absolute; left: 33px; top: 60px;
    display: flex; align-items: center; gap: 8px;
    font-size: 33px; font-weight: 400; letter-spacing: -0.5px;
    color: var(--ink);
  }
  .brand__dot { width: 10px; height: 10px; border-radius: 50%; background: var(--brand-red); }
  .headline { position: absolute; left: 33px; top: 175px; line-height: 1; }
  .headline span { display: block; font-weight: 400; }
  .headline__line { font-size: 47px; margin-bottom: 4px; letter-spacing: -0.5px; }
  .headline__pizza { font-size: 62px; color: var(--brand-red); margin-bottom: 2px; }
  .headline__sizes { font-size: 47px; }
  .rule { position: absolute; left: 40px; top: 398px; width: 206px; height: 4px; background: var(--rule-red); }

  .price-list { position: absolute; left: 33px; list-style: none; }
  .price-row { display: grid; grid-template-columns: 217px 80px 80px; font-size: 15.5px; line-height: 20px; text-transform: uppercase; }
  .price-list--classic { top: 424px; }
  .price-list--specialty { top: 652px; }
  .price-list--specialty .price-row { line-height: 17px; margin-bottom: 14px; }
  .price-row small { display: block; font-size: 8.5px; line-height: 10px; text-transform: none; }

  .band {
    position: absolute; left: 0; top: 606px;
    width: 434px; height: 30px;
    background: var(--brand-red); color: var(--on-red);
    font-size: 19px; line-height: 30px; padding-left: 33px;
    text-transform: uppercase;
  }

  /* ---------- back ---------- */
  .page--back { left: 623px; width: 499px; background: var(--menu-red); color: var(--on-red); }
  .full-menu { position: absolute; left: 34px; top: 46px; list-style: none; }
  .menu-item {
    display: grid; grid-template-columns: 256px 78px 90px;
    margin-bottom: 2.2px;
  }
  .menu-item__name { font-size: 15px; line-height: 15px; text-transform: uppercase; }
  .menu-item__price { font-size: 10px; line-height: 15px; }
  .menu-item__desc {
    grid-column: 1; font-size: 8.5px; line-height: 9.6px;
    color: var(--on-red-soft); width: 230px;
  }
  .menu-item__extra { grid-column: 2 / span 2; font-size: 10px; line-height: 12px; align-self: end; }
</style>
</head>
<body>

<section class="page page--front">
  <div class="hero-art" role="img" aria-label="Hand-drawn pizza illustration with tomato, basil and olives"></div>

  <div class="brand"><span>CALDER PIZZA</span><span class="brand__dot"></span></div>

  <h1 class="headline">
    <span class="headline__line">CLASSIC</span>
    <span class="headline__line">TAKE-OUT</span>
    <span class="headline__pizza">PIZZA</span>
    <span class="headline__sizes">8" &amp; 13"</span>
  </h1>
  <div class="rule"></div>

  <ul class="price-list price-list--classic">
    <li class="price-row"><span>Pepperoni &amp; Mushroom</span><span>$12.99</span><span>$30.95</span></li>
    <li class="price-row"><span>Pepperoni</span><span>$11.99</span><span>$29.95</span></li>
    <li class="price-row"><span>Hawaiian</span><span>$12.99</span><span>$30.95</span></li>
    <li class="price-row"><span>Beef &amp; Mushroom</span><span>$13.49</span><span>$32.95</span></li>
    <li class="price-row"><span>Pepperoni &amp; Ham</span><span>$12.99</span><span>$30.95</span></li>
    <li class="price-row"><span>Ham &amp; Mushroom</span><span>$12.99</span><span>$30.95</span></li>
    <li class="price-row"><span>Beef &amp; Onion</span><span>$13.49</span><span>$32.95</span></li>
    <li class="price-row"><span>Cheese</span><span>$11.99</span><span>$29.95</span></li>
  </ul>

  <h2 class="band">Specialty Take-Out Pizza- 8" &amp; 13"</h2>

  <ul class="price-list price-list--specialty">
    <li class="price-row"><span>All Meat<small>Pepperoni, Beef &amp; Smoked Ham &amp; Bacon</small></span><span>$14.99</span><span>$35.95</span></li>
    <li class="price-row"><span>Double Pepperoni<small>Loads of Pepperoni</small></span><span>$13.49</span><span>$32.95</span></li>
    <li class="price-row"><span>Hot Honey Pepperoni<small>Double Pepperoni and drizzled with Hot Honey</small></span><span>$14.49</span><span>$34.95</span></li>
    <li class="price-row"><span>Hawaiian Heat<small>Smoked Ham, Pineapple and Banana Peppers</small></span><span>$13.49</span><span>$32.95</span></li>
    <li class="price-row"><span>Four Cheese<small>Mozzarella, Feta, Romano and Cheddar Cheese</small></span><span>$13.49</span><span>$32.95</span></li>
  </ul>
</section>

<section class="page page--back">
  <ul class="full-menu">
    <li class="menu-item"><span class="menu-item__name">Montreal</span><span class="menu-item__price">$13.49</span><span class="menu-item__price">$32.95</span><span class="menu-item__desc">Pepperoni &amp; Double Smoked Bacon</span></li>
    <li class="menu-item"><span class="menu-item__name">Montreal Heat</span><span class="menu-item__price">$13.99</span><span class="menu-item__price">$33.95</span><span class="menu-item__desc">Pepperoni, Double Smoked Bacon &amp; Banana Peppers</span></li>
    <li class="menu-item"><span class="menu-item__name">Supreme</span><span class="menu-item__price">$13.49</span><span class="menu-item__price">$32.95</span><span class="menu-item__desc">Pepperoni, Mushrooms &amp; Green Peppers</span></li>
    <li class="menu-item"><span class="menu-item__name">Canadian</span><span class="menu-item__price">$13.49</span><span class="menu-item__price">$32.95</span><span class="menu-item__desc">Pepperoni, Mushrooms &amp; Ham</span></li>
    <li class="menu-item"><span class="menu-item__name">BBQ Chicken</span><span class="menu-item__price">$13.99</span><span class="menu-item__price">$33.95</span><span class="menu-item__desc">Chicken Breast, Hickory BBQ Sauce &amp; Red Onions.</span></li>
    <li class="menu-item"><span class="menu-item__name">BBQ Chicken Plus</span><span class="menu-item__price">$14.79</span><span class="menu-item__price">$34.95</span><span class="menu-item__desc">Chicken Breast, Hickory BBQ Sauce, Red Onions &amp; Cilantro</span></li>
    <li class="menu-item"><span class="menu-item__name">Spicy BBQ Chicken</span><span class="menu-item__price">$14.49</span><span class="menu-item__price">$35.95</span><span class="menu-item__desc">Chicken Breast, Hickory BBQ Sauce, Red Onions &amp; Banana Peppers</span></li>
    <li class="menu-item"><span class="menu-item__name">Sweet Chili Chicken</span><span class="menu-item__price">$14.49</span><span class="menu-item__price">$35.95</span><span class="menu-item__desc">Chicken Breast, Pineapple, Red Onions &amp; Sweet Chili Sauce</span></li>
    <li class="menu-item"><span class="menu-item__name">Chicken Club</span><span class="menu-item__price">$14.79</span><span class="menu-item__price">$35.95</span><span class="menu-item__desc">Chicken Breast, Double Smoked Bacon, Red Onions and Tomatoes</span></li>
    <li class="menu-item"><span class="menu-item__name">Athenean</span><span class="menu-item__price">$14.49</span><span class="menu-item__price">$34.95</span><span class="menu-item__desc">Chicken Breast, Spinach, Feta Cheese and Tomato</span></li>
    <li class="menu-item"><span class="menu-item__name">Greek Supreme</span><span class="menu-item__price">$14.99</span><span class="menu-item__price">$35.95</span><span class="menu-item__desc">Chicken Breast, Feta Cheese, Tomato, Green Pepper, Red Onions &amp; Black Olives</span></li>
    <li class="menu-item"><span class="menu-item__name">Mediterranean Chicken</span><span class="menu-item__price">$14.79</span><span class="menu-item__price">$35.95</span><span class="menu-item__desc">Seasoned Chicken Breast, Tomatoes, Red Onions and Feta Cheese</span></li>
    <li class="menu-item"><span class="menu-item__name">Original Spinach</span><span class="menu-item__price">$13.49</span><span class="menu-item__price">$32.95</span><span class="menu-item__desc">Spinach &amp; Feta Cheese</span></li>
    <li class="menu-item"><span class="menu-item__name">Zeus</span><span class="menu-item__price">$13.95</span><span class="menu-item__price">$33.95</span><span class="menu-item__desc">Spinach, Feta Cheese and Tomatoes</span></li>
    <li class="menu-item"><span class="menu-item__name">Greek</span><span class="menu-item__price">$13.99</span><span class="menu-item__price">$33.95</span><span class="menu-item__desc">Feta Cheese, Tomato, Green Peppers, Red Onions and Black Olives</span></li>
    <li class="menu-item"><span class="menu-item__name">Vegetarian</span><span class="menu-item__price">$13.49</span><span class="menu-item__price">$32.95</span><span class="menu-item__desc">Mushrooms, Tomatoes, Green Peppers and Black Olives</span></li>
    <li class="menu-item"><span class="menu-item__name">Veggie Delight</span><span class="menu-item__price">$13.95</span><span class="menu-item__price">$33.95</span><span class="menu-item__desc">Mushrooms, Tomatoes, Green Peppers, Black Olives &amp; Onions</span></li>
    <li class="menu-item"><span class="menu-item__name">Deluxe</span><span class="menu-item__price">$13.95</span><span class="menu-item__price">$33.95</span><span class="menu-item__desc">Pepperoni, Mushrooms, Ham, Tomatoes, Green Peppers and Red Onions</span></li>
    <li class="menu-item"><span class="menu-item__name">Calder Special</span><span class="menu-item__price">$14.49</span><span class="menu-item__price">$34.95</span><span class="menu-item__desc">Pepperoni, Mushrooms, Ham, Green Peppers and Black Olives</span></li>
    <li class="menu-item"><span class="menu-item__name">Dill Pickle</span><span class="menu-item__price">$14.49</span><span class="menu-item__price">$34.95</span><span class="menu-item__desc">Crispy Dill Pickles, Fresh Dill with our cream based garlic sauce. Served with our without bacon.</span><span class="menu-item__extra">$13.49 &nbsp;&nbsp;&nbsp;&nbsp;&nbsp;&nbsp;&nbsp;&nbsp;&nbsp;&nbsp;&nbsp;$32.95 / $14.49 $35.95</span></li>
    <li class="menu-item"><span class="menu-item__name">BBQ Pulled Pork</span><span class="menu-item__price">$14.49</span><span class="menu-item__price">$35.95</span><span class="menu-item__desc">Pulled Pork, Red Onions, Red Peppers and Cilantro.</span></li>
  </ul>
</section>

</body>
</html>
```